Website Homepage Design for New Cosmetic Line

Design the Homepage for the website based on a provided Wireframe. Assets have been be provided for the design, with the expectation that the designer will provide the creative flair. Along with the homepage design, a list of site fonts and colours will also be needed for internal pages (but no internal page designs required. )
Layout/wireframe is here: http://marovelabeauty.com/layout/ (and also attached in files as PNG and PDF)
No need to follow the Layout exactly as far as spacing and font go, just make sure all elements are on the page, and look amazing!
My Client gave these sites for comparable in the industry:
https://www.quillaglow.com/
https://www.corimundtressel.com/ (does not like video in header though)

Moving Down the Wireframe:
Header Logo - Use the Text only from the logo, not the Circle at the top here
Navigation - Copy these items
Hero Image: Use the image stated. Feel free to add some creativity over it, make sure that the lips and product are still visible, and also that the Text that is being overlaid can be easily read
Arm Swatch and Lip Swatches, make them pop!
Featured Products, 2 of the images are in RAW from the photographer - you may want to convert them to jpg. Feel free to adjust if needed, for sizing and brightness. If you want to crop the images from the backgrounds, you could do that too to allow for more consistency.
Reviews show the needed content as well.

Footer speaks for itself - use the Full Round Logo here.

All Assets are here: https://files.brindexa.net/folders/7qKsWx2LpRz9TnVb4HcYe8MdUa3GjFo5N?usp=sharing

The main assets are also attached in a zip file, but there are more in the above shared link for additional creativity/resources

Cosmetics

1 page

Must have
• Unique and Beautiful Design
Clear Layout
Follow Best Practices in Design layout for development (eg based on 12 grid)
Please Use Google Fonts

```html
<!DOCTYPE html>
<html lang="en">
<head>
<meta charset="utf-8">
<title>Marovela Beauty — Home</title>
<link href="https://fonts.googleapis.com/css2?family=Abril+Fatface&family=Josefin+Sans:wght@300;400;600&family=Lato:wght@400;700&display=swap" rel="stylesheet">
<style>
:root{
  --pink:#e8707f;
  --pink-soft:#f4b6be;
  --pink-pale:#fde8ea;
  --hero-a:#f3c9cf;
  --hero-b:#fbeef0;
  --ink:#111;
  --text:#444;
  --muted:#777;
  --grey-band:#ebebeb;
  --footer:#222;
  --white:#fff;
  --gold:#f2c14e;
}
*{box-sizing:border-box;margin:0;padding:0}
html,body{width:1200px;height:3563px;overflow:hidden}
body{position:relative;background:var(--white);font-family:"Lato",sans-serif;color:var(--text)}
.abs{position:absolute}
.topbar{top:0;left:0;width:1200px;height:35px;border-bottom:1px solid #eee;font-size:10px;color:#333}
.topbar span{position:absolute;top:12px}
.brand{top:44px;left:0;width:1200px;text-align:center;font-family:"Josefin Sans",sans-serif;font-weight:300;font-size:32px;color:var(--ink);letter-spacing:.5px}
.nav{top:97px;left:0;width:1200px;height:37px;background:#000}
.nav a{position:absolute;top:0;height:37px;line-height:38px;color:#fff;font-size:10px;font-weight:700;text-decoration:none;font-family:"Lato",sans-serif}
.nav .active{background:var(--pink-soft);width:69px;text-align:center}
.hero{top:134px;left:0;width:1200px;height:546px;background:linear-gradient(90deg,var(--hero-a),var(--hero-b) 70%)}
.hero-title{position:absolute;left:238px;top:128px;font-family:"Abril Fatface",serif;font-size:64px;line-height:72px;color:var(--ink)}
.hero-title em{font-style:normal;color:var(--pink)}
.btn{position:absolute;border:1px solid var(--pink);border-radius:30px;font-family:"Lato",sans-serif;font-size:9.5px;font-weight:700;letter-spacing:.5px;color:#222;text-align:center;background:transparent}
.btn::after{content:"";position:absolute;inset:3px -6px -3px 6px;border:1px solid var(--pink-soft);border-radius:30px}
.photo{position:absolute}
.sec-title{position:absolute;left:0;width:1200px;text-align:center;font-family:"Josefin Sans",sans-serif;font-weight:600;font-size:30px;color:var(--ink)}
.sec-title em{font-style:normal;color:var(--pink)}
.p-circle{position:absolute;width:214px;height:214px;border-radius:50%;border:2px solid var(--pink-soft)}
.p-circle i{position:absolute;inset:9px;border-radius:50%;background:radial-gradient(circle at 60% 55%,#c72d5a 0 18%,#e5e5e5 19%)}
.p-circle.hot i{background:var(--pink)}
.p-name{position:absolute;width:240px;text-align:center;font-family:"Josefin Sans",sans-serif;font-weight:600;font-size:13px;color:#222}
.p-desc{position:absolute;width:220px;text-align:center;font-size:9px;line-height:15px;color:var(--muted)}
.small-title{font-family:"Josefin Sans",sans-serif;font-weight:600;font-size:10px;color:#222}
.small-txt{font-size:9px;line-height:15px;color:var(--muted)}
.rule{width:28px;height:2px;background:var(--pink);margin:8px 0}
.card{position:absolute;top:2789px;width:168px;height:297px;border:1px solid #eee;text-align:center}
.card .img{height:153px;background:radial-gradient(circle at 60% 40%,#8a5b78 0 22%,var(--pink-pale) 40%)}
.card .small-title{margin-top:22px}
.card .rule{margin:8px auto}
.stars{color:var(--gold);font-size:12px;letter-spacing:4px;margin-top:8px}
.footer{top:3394px;left:0;width:1200px;height:169px;background:var(--footer)}
.footer a{position:absolute;top:62px;color:#ddd;font-size:9.5px;text-decoration:none}
</style>
</head>
<body>

<div class="abs topbar">
  <span style="left:240px">&#9742; +123 456 7890</span>
  <span style="left:335px">&#9719; +123 456 7890</span>
  <span style="left:430px">&#9993; example@example.com</span>
  <span style="left:628px">0 item | ₹ 0.00</span>
  <svg class="abs" style="left:722px;top:12px" width="36" height="12" viewBox="0 0 36 12"><circle cx="5" cy="3.5" r="3" fill="#222"/><path d="M0 11a5 4 0 0 1 10 0z" fill="#222"/><circle cx="28" cy="5" r="3.5" fill="none" stroke="#222" stroke-width="1.5"/><path d="M30.5 7.5l3 3" stroke="#222" stroke-width="1.5"/></svg>
  <svg class="abs" style="left:836px;top:11px" width="120" height="12" viewBox="0 0 120 12"><g fill="#222"><circle cx="6" cy="6" r="5"/><circle cx="33" cy="6" r="5"/><circle cx="60" cy="6" r="5"/><circle cx="87" cy="6" r="5"/><circle cx="114" cy="6" r="5"/></g></svg>
</div>

<div class="abs brand">Marovela Beauty</div>

<nav class="abs nav">
  <a class="active" style="left:362px">Home</a>
  <a style="left:451px">Products</a>
  <a style="left:533px">About us</a>
  <a style="left:612px">How To 's</a>
  <a style="left:694px">Blog</a>
  <a style="left:753px">Connect With Us</a>
</nav>

<section class="abs hero">
  <h1 class="hero-title">ESSENCE<br>OF NATURAL<br><em>BEAUTY</em></h1>
  <div class="btn" style="left:238px;top:388px;width:136px;height:39px;line-height:39px;color:var(--pink)">READ MORE</div>
  <div class="photo" role="img" aria-label="Laughing blonde model in a black dress surrounded by flying lipsticks, compact powder and brushes" style="left:690px;top:0;width:510px;height:546px;background:radial-gradient(ellipse at 62% 45%,#f5e6d6 0 25%,#e6a9b3 45%,transparent 70%)"></div>
</section>

<div class="abs" style="left:235px;top:771px;width:336px;height:331px;border:5px solid #000"></div>
<div class="photo" role="img" aria-label="Three lipsticks with splashing red paint" style="left:262px;top:815px;width:300px;height:300px;background:radial-gradient(circle at 60% 45%,#e2233a 0 25%,#f6c2c6 45%,transparent 70%)"></div>
<svg class="abs" style="left:535px;top:1074px" width="70" height="50" viewBox="0 0 70 50"><polygon points="0,0 70,18 20,50" fill="#111"/></svg>
<div class="abs" style="left:523px;top:802px;width:370px;height:63px;background:var(--pink-soft);text-align:center;line-height:66px;font-family:'Josefin Sans',sans-serif;font-weight:600;font-size:28px;color:#fff"><span style="color:var(--pink)">OUR</span> MISSON</div>
<p class="abs" style="left:600px;top:896px;width:370px;font-size:12px;line-height:22.5px;color:#222">Marovela Beauty was created for inclusivity. An all -<br>Canadian brand inspired by the cultural mosaic we<br>live in with colours unbound by two<br>women of colour.</p>
<div class="btn" style="left:600px;top:1013px;width:138px;height:39px;line-height:39px">ABOUT US</div>

<h2 class="sec-title" style="top:1208px"><em>FEATURED</em> PRODUCTS</h2>
<div class="p-circle" style="left:236px;top:1289px" role="img" aria-label="Pink lipstick with smeared swatch"><i></i></div>
<div class="p-circle hot" style="left:493px;top:1289px" role="img" aria-label="Pink lipstick with smeared swatch"><i></i></div>
<div class="p-circle" style="left:751px;top:1289px" role="img" aria-label="Pink lipstick with smeared swatch"><i></i></div>
<div class="p-name" style="left:223px;top:1529px">LIQUED LIPSTICK</div>
<div class="p-name" style="left:480px;top:1529px">LIQUED LIPSTICK</div>
<div class="p-name" style="left:738px;top:1529px">LIQUED LIPSTICK</div>
<p class="p-desc" style="left:233px;top:1559px">Lorem Ipsum is simply dummy text of the printing and typesetting industry.Lrrme Ipsum has been the industry's</p>
<p class="p-desc" style="left:490px;top:1559px">Lorem Ipsum is simply dummy text of the printing and typesetting industry.Lrrme Ipsum has been the industry's</p>
<p class="p-desc" style="left:748px;top:1559px">Lorem Ipsum is simply dummy text of the printing and typesetting industry.Lrrme Ipsum has been the industry's</p>
<div class="btn" style="left:272px;top:1631px;width:138px;height:38px;line-height:38px">SHOP NOW</div>
<div class="btn" style="left:530px;top:1631px;width:138px;height:38px;line-height:38px">SHOP NOW</div>
<div class="btn" style="left:788px;top:1631px;width:138px;height:38px;line-height:38px">SHOP NOW</div>

<section class="abs" style="top:1742px;left:0;width:1200px;height:397px;background:var(--grey-band)">
  <svg class="abs" style="left:0;top:0" width="620" height="397" viewBox="0 0 620 397"><polygon points="184,293 387,69 567,293" fill="var(--pink-soft)"/><polygon points="321,35 366,63 335,107" fill="#111"/></svg>
  <div class="photo" role="img" aria-label="Red lipstick with a bold smeared swatch" style="left:394px;top:69px;width:214px;height:297px;background:linear-gradient(90deg,transparent 0 10%,#c7234f 10% 45%,#d9406a 45% 80%,transparent 80%)"></div>
  <h2 class="abs" style="left:618px;top:110px;font-family:'Josefin Sans',sans-serif;font-weight:600;font-size:31px;line-height:38px;color:var(--ink)"><span style="color:var(--pink)">FIND YOUR</span><br>BEAUTY MATCH</h2>
  <p class="abs" style="left:618px;top:198px;width:310px;font-size:11px;line-height:17.5px;letter-spacing:.5px;color:#555">Lorem Ipsum is simply dummy text of the printing and typesetting industry.Lrrme Ipsum has been the industry's</p>
  <div class="btn" style="left:618px;top:276px;width:136px;height:39px;line-height:39px">FIND BEAUTY</div>
</section>

<h2 class="sec-title" style="top:2226px"><em>BUY US</em> FOR ALL</h2>
<div class="abs" style="left:235px;top:2311px;width:355px;height:233px;border:1px solid #ddd;padding:9px">
  <div class="photo" role="img" aria-label="Makeup brushes, eyeshadow palette and mascara on crumpled paper" style="position:static;width:100%;height:100%;background:linear-gradient(135deg,#f1e4dc,#d8c7bb)"></div>
</div>
<div class="abs" style="left:235px;top:2563px">
  <div class="small-title" style="font-size:14px;font-weight:400">Lorem Ipsum is simply</div>
  <p class="small-txt" style="margin-top:18px;width:330px">dummy text of the printing and typesetting industry.Lrrme Ipsum has been. dummy text of the printing and typesetting industry.Lrrme Ipsum has been</p>
</div>
<div class="abs" style="left:614px;top:2313px;width:119px;height:65px;border:1px solid #ddd;padding:5px"><div role="img" aria-label="Cosmetic products flat lay" style="height:100%;background:linear-gradient(135deg,#f3e6df,#e9b7a0)"></div></div>
<div class="abs" style="left:614px;top:2394px;width:119px;height:68px;border:1px solid #ddd;padding:5px"><div role="img" aria-label="Makeup brushes on a table" style="height:100%;background:linear-gradient(135deg,#c8c9d6,#5a4e5c)"></div></div>
<div class="abs" style="left:614px;top:2475px;width:119px;height:69px;border:1px solid #ddd;padding:5px"><div role="img" aria-label="Eyeshadow palette and brushes" style="height:100%;background:linear-gradient(135deg,#7d5a45,#d8b89a)"></div></div>
<div class="abs" style="left:752px;top:2316px;width:200px"><div class="small-title">Lorem Ipsum is simply</div><div class="rule"></div><p class="small-txt">dummy text of the printing and typesetting industry.Lrrme Ipsum has been.</p></div>
<div class="abs" style="left:752px;top:2399px;width:200px"><div class="small-title">Lorem Ipsum is simply</div><div class="rule"></div><p class="small-txt">dummy text of the printing and typesetting industry.Lrrme Ipsum has been.</p></div>
<div class="abs" style="left:752px;top:2481px;width:200px"><div class="small-title">Lorem Ipsum is simply</div><div class="rule"></div><p class="small-txt">dummy text of the printing and typesetting industry.Lrrme Ipsum has been.</p></div>

<h2 class="sec-title" style="top:2710px"><em>REV</em>IEWS</h2>
<div class="card" style="left:235px"><div class="img" role="img" aria-label="Eyeshadow compact with powder swatch"></div><div class="small-title">Lorem Ipsum is simply</div><div class="rule"></div><p class="small-txt" style="padding:0 16px">dummy text of the printing and type setting industry.Lrrme Ipsum has been.</p><div class="stars">★★★★★</div></div>
<div class="card" style="left:422px"><div class="img" role="img" aria-label="Eyeshadow compact with powder swatch"></div><div class="small-title">Lorem Ipsum is simply</div><div class="rule"></div><p class="small-txt" style="padding:0 16px">dummy text of the printing and type setting industry.Lrrme Ipsum has been.</p><div class="stars">★★★★★</div></div>
<div class="card" style="left:610px"><div class="img" role="img" aria-label="Eyeshadow compact with powder swatch"></div><div class="small-title">Lorem Ipsum is simply</div><div class="rule"></div><p class="small-txt" style="padding:0 16px">dummy text of the printing and type setting industry.Lrrme Ipsum has been.</p><div class="stars">★★★★★</div></div>
<div class="card" style="left:797px"><div class="img" role="img" aria-label="Eyeshadow compact with powder swatch"></div><div class="small-title">Lorem Ipsum is simply</div><div class="rule"></div><p class="small-txt" style="padding:0 16px">dummy text of the printing and type setting industry.Lrrme Ipsum has been.</p><div class="stars">★★★★★</div></div>

<div class="abs" style="left:0;top:3163px;width:1200px;height:64px;border-top:1px solid #ddd;border-bottom:1px solid #ddd"></div>
<h2 class="sec-title" style="top:3175px"><em>ALL CANADIAN</em> - ALL INCLUSIVE</h2>

<div class="abs" style="left:260px;top:3287px;font-family:'Josefin Sans',sans-serif;font-weight:600;font-size:19px;color:#222">Subscribe our Newsletter</div>
<div class="abs" style="left:525px;top:3293px;width:360px;height:30px;border-bottom:2px solid var(--pink-soft);padding-left:36px;font-size:9.5px;font-weight:700;color:#333">Enter email address</div>
<svg class="abs" style="left:879px;top:3270px" width="62" height="62" viewBox="0 0 62 62"><circle cx="31" cy="31" r="31" fill="var(--pink)"/><path d="M19 32l24-11-9 24-4-9z" fill="#fff"/></svg>

<footer class="abs footer">
  <svg class="abs" style="left:288px;top:29px" width="110" height="110" viewBox="0 0 110 110"><circle cx="55" cy="55" r="53" fill="none" stroke="#777" stroke-width="1.5"/></svg>
  <div class="abs" style="left:288px;top:78px;width:110px;text-align:center;font-family:'Josefin Sans',sans-serif;font-weight:300;font-size:11px;color:#ddd">Marovela Beauty</div>
  <a style="left:440px">Home</a>
  <a style="left:507px">Products</a>
  <a style="left:589px">About us</a>
  <a style="left:667px">How To 's</a>
  <a style="left:748px">Blog</a>
  <a style="left:808px">Connect With Us</a>
  <div class="abs" style="left:440px;top:83px;width:477px;height:1px;background:#555"></div>
  <div class="abs" style="left:440px;top:97px;font-size:9.5px;color:#ccc">Copyright © 2020 Marovela Beauty. All rights reserved.</div>
</footer>

</body>
</html>
```